Career Counselor in need of a business card design

Hello Creatives! I'm in need of a business card design for a new company based in Georgia, USA called Pathways By Lantern.

Some things that may be helpful in creating your concept(s) include:

My Logo (Included in the Files section): There are three versions, two versions are in the second file. The all gold stacked (vertical) version is my primary logo and then there are two horizontal versions (one is all gold and the other is gold and grey).

My mission: to empower tweens through young adults to realize and actualize their CAREER ASPIRATIONS.
My vision: for tweens through young adults to LIVE LIFE ON PURPOSE and become CONTRIBUTING MEMBERS OF SOCIETY.

Biblical scriptures that support my ‘Why’: Psalms 127: 3-4(NIV) Children are a heritage from the Lord, offspring a reward from him. Like ARROWS in the hands of a warrior are children…. And Proverbs 29:18(JKV) Where there is no VISION, the people perish.

*Words in ALL CAPS are to emphasize what's important to me and may possibly provide you some inspiration (IDK - Have fun with it)!

Target Market(s)

My ideal customers are parents, guardians, and young adults.

Contact Information for Business Card

My name, degrees and credential: Delphine Marlow, M.S., Ed.S., NCC
Title: College and Career Coach and Consultant

Number: 555.318.2907
Address: 2718 Willowmere Avenue., Suite 405, Macon, GA 31299
Email: info@pathwaysbylantern.example
Website: www.pathwaysbylantern.example

My population: TWEENS • TEENS • EMERGING ADULTS
Services offered: One-On-One Sessions • Small Groups • Workshops

Colors

Designer to choose colors to be used in the design.

Requirements
Nice to have
• Either my mission or vision but I will understand if it does not all fit.
• My mission: To empower tweens through young adults to realize and actualize their career aspirations.
• My vision: For tweens through young adults to live life on purpose and become contributing members of society.

```html
<!DOCTYPE html>
<html lang="en">
<head>
<meta charset="utf-8">
<title>Pathways By Lantern – Business Card</title>
<link href="https://fonts.googleapis.com/css2?family=Cinzel:wght@500&family=Oswald:wght@300;400&display=swap" rel="stylesheet">
<style>
  :root {
    --page: #ececec;
    --front-bg: #232323;
    --back-bg: #464646;
    --gold: #d9b24a;
    --gold-light: #f0d27a;
    --gold-faint: rgba(217, 178, 74, 0.08);
  }
  * { box-sizing: border-box; margin: 0; padding: 0; }
  html, body { width: 1200px; height: 1200px; overflow: hidden; }
  body { background: var(--page); position: relative; font-family: 'Oswald', sans-serif; }

  .card {
    position: absolute;
    left: 282px;
    width: 696px;
    height: 416px;
    border-radius: 12px;
    overflow: hidden;
  }
  .card--front { top: 106px; background: var(--front-bg); }
  .card--back { top: 636px; background: var(--back-bg); }

  .wordmark { font-family: 'Cinzel', serif; font-weight: 500; color: var(--gold); line-height: 1; }
  .wordmark__main { display: block; font-size: 56px; letter-spacing: 1px; }
  .wordmark__sub { display: block; font-size: 27px; letter-spacing: 6px; margin-top: 2px; }

  /* Front */
  .front__ring-faint { position: absolute; left: 300px; top: -10px; width: 380px; height: 380px; border-radius: 50%; border: 26px solid var(--gold-faint); }
  .front__mark { position: absolute; left: 102px; top: 152px; width: 108px; height: 108px; border-radius: 50%; border: 6px solid var(--gold); }
  .front__divider { position: absolute; left: 262px; top: 130px; width: 2px; height: 150px; background: linear-gradient(var(--gold-faint), var(--gold), var(--gold-faint)); }
  .front__wordmark { position: absolute; left: 284px; top: 160px; }
  .front__wordmark .wordmark__main { font-size: 50px; }
  .front__wordmark .wordmark__sub { font-size: 24px; letter-spacing: 5px; }
  .front__services { position: absolute; left: 0; right: 0; top: 376px; text-align: center; color: var(--gold); font-size: 11px; font-weight: 400; letter-spacing: .3px; }

  /* Back */
  .back__wordmark { position: absolute; left: 54px; top: 56px; }
  .back__mission { position: absolute; left: 40px; width: 320px; top: 176px; text-align: center; color: var(--gold); font-size: 14px; line-height: 21px; letter-spacing: .4px; }
  .back__name { position: absolute; left: 48px; top: 284px; color: var(--gold); font-size: 18px; font-weight: 400; letter-spacing: .6px; }
  .back__title { position: absolute; left: 48px; top: 309px; color: var(--gold); font-size: 14px; letter-spacing: .4px; }
  .back__rule { position: absolute; left: 48px; top: 331px; width: 318px; height: 1px; background: var(--gold); }
  .contact { position: absolute; left: 48px; top: 341px; list-style: none; color: var(--gold); font-size: 12px; font-weight: 300; }
  .contact li { display: flex; align-items: center; gap: 10px; height: 22px; }
  .contact svg { width: 13px; height: 13px; fill: var(--gold); flex: none; }
  .back__mark { position: absolute; left: 432px; top: 96px; width: 210px; height: 210px; border-radius: 50%; border: 8px solid var(--gold); }
  .back__band { position: absolute; left: 0; bottom: 0; width: 696px; height: 30px; }
  .back__website { position: absolute; right: 22px; bottom: 7px; color: #3a3a3a; font-size: 11px; letter-spacing: .4px; }
</style>
</head>
<body>
  <section class="card card--front">
    <div class="front__ring-faint"></div>
    <div class="front__mark"></div>
    <div class="front__divider"></div>
    <div class="wordmark front__wordmark">
      <span class="wordmark__main">PATHWAYS</span>
      <span class="wordmark__sub">BY LANTERN</span>
    </div>
    <p class="front__services">One-On-One Sessions ▪ Small Groups ▪ Workshops</p>
  </section>

  <section class="card card--back">
    <div class="wordmark back__wordmark">
      <span class="wordmark__main">PATHWAYS</span>
      <span class="wordmark__sub">BY LANTERN</span>
    </div>
    <p class="back__mission">Empower Tweens Through Young Adults To Realize And Actualize Their Career Aspirations.</p>
    <p class="back__name">Delphine Marlow, M.S., Ed.S., NCC</p>
    <p class="back__title">College and Career Coach and Consultant</p>
    <div class="back__rule"></div>
    <ul class="contact">
      <li><svg viewBox="0 0 24 24"><path d="M6.6 10.8a15.1 15.1 0 0 0 6.6 6.6l2.2-2.2a1 1 0 0 1 1-.25 11.4 11.4 0 0 0 3.6.57 1 1 0 0 1 1 1V20a1 1 0 0 1-1 1A17 17 0 0 1 3 4a1 1 0 0 1 1-1h3.5a1 1 0 0 1 1 1c0 1.25.2 2.45.57 3.57a1 1 0 0 1-.25 1z"/></svg>555.318.2907</li>
      <li><svg viewBox="0 0 24 24"><path d="M2 5h20v2l-10 6L2 7z M2 9l10 6 10-6v10H2z"/></svg>info@pathwaysbylantern.example</li>
      <li><svg viewBox="0 0 24 24"><path d="M12 2a7 7 0 0 0-7 7c0 5.2 7 13 7 13s7-7.8 7-13a7 7 0 0 0-7-7zm0 9.5A2.5 2.5 0 1 1 12 6.5a2.5 2.5 0 0 1 0 5z"/></svg>2718 Willowmere Avenue., Suite 405, Macon, GA 31299</li>
    </ul>
    <div class="back__mark"></div>
    <svg class="back__band" viewBox="0 0 696 30" preserveAspectRatio="none">
      <defs>
        <linearGradient id="bandGold" x1="0" x2="1">
          <stop offset="0" stop-color="#b8912f"/>
          <stop offset="0.6" stop-color="#f0d27a"/>
          <stop offset="1" stop-color="#d9b24a"/>
        </linearGradient>
      </defs>
      <path d="M0 24 H450 C462 24 466 6 480 6 H696 V30 H0 Z" fill="url(#bandGold)"/>
    </svg>
    <span class="back__website">www.pathwaysbylantern.example</span>
  </section>
</body>
</html>
```